Modern Website Design for an Online Travel Agency.. Design Only!!

Hi there!

We are building an website for our travel agency that caters to tourists traveling to the Cayman Islands. We provide travel information and take bookings for various tours available here.

We need designs for 8 different web page layouts. You can see the layout specifications in two attached documents. We do not have a need for the coding to be done. This will simply act as a blueprint for our developer to build from.

The important pages are the 'Home Page' 'checkout page' and the ‘Checkout Page’ (Page 1 & 10 in the PDF ‘Website Layout’)

The MOST important page is ‘Tour Search Page’ (page 6)

If you intend on only submitting one page design, please submit a design for page 6. Be aware though, the more of these 3 page designs you submit, the more likely we are to move forward with you!

At this stage, we are simply looking to develop the most aesthetic website design layout possible.

- The website should be colour coordinated with the logo. You can most certainly use other colours if you feel they complement the overall design of the website well.

- Everything must be laid out in an EXTREMELY simple & ‘easy to navigate’ way. The key is simplicity & Functionality. There is no need for messy or elaborate graphics.

- The website MUST have a VERY clean and modern appearance.

- We want the main background to be white, but you can use light grey in places to compliment or add dimension if you feel necessary.

- We will appreciate a good use of shadows and especially a good use of icons. (You can see examples of icons we have already designed, we are definitely open to new icon design concepts too)

- We will reward imagination and original thinking! Essentially we want a website with a creative touch and unique design elements, whilst maintaining that clean and simple layout.

- Most importantly!! - Paying attention to the small details will be highly rewarded (A well balanced and seamless use of fonts, colours, dimensions, shadowing, positioning, etc)

If you have any questions, please don’t hesitate to ask.

We’re excited to see your design submissions!

Thank you!!

You can find all the support documents and content at: https://www.filevorra.net/sh/9qm2rtwplexan7c/QQBmTtZnPdLsWEGxvvaJpLmRw?dl=0

Target Market(s)

Tourists

Industry/Entity Type

Travel

Number of Pages Required

5+ page

Font styles to use
Sans Serif

Colors

Designer to choose colors to be used in the design.

Requirements
Must have
• Must be very clean and modern.
• Must be simple and bold
• Must be color coordinated in a way that makes sense
• White background
Nice to have
• Good use of shadows and Icons
Should not have
• Over use of messy graphics
• And design layout which is not right angled (using anything but vertical or horizontal for the edges in the design)

```html
<!DOCTYPE html>
<html lang="en">
<head>
<meta charset="utf-8">
<title>IsleRoute – Cayman Islands</title>
<link href="https://fonts.googleapis.com/css2?family=Roboto:wght@400;500;700;900&display=swap" rel="stylesheet">
<style>
  :root{
    --blue:#0a6fd8;
    --navy:#0b3fa6;
    --green:#8dc63f;
    --topbar:#e6eef8;
    --text:#222;
    --muted:#666;
    --line:#9a9a9a;
    --field:#efefef;
  }
  *{box-sizing:border-box;margin:0;padding:0}
  html,body{width:1200px;height:1200px;overflow:hidden;background:#fff;font-family:'Roboto',sans-serif;color:var(--text)}
  .page{position:relative;width:1200px;height:1200px}
  .frame{position:absolute;left:55px;width:1095px}
  .topbar{top:0;height:38px;background:var(--topbar)}
  .social{position:absolute;left:683px;top:12px;display:flex;gap:14px}
  .social span{width:13px;height:13px;border-radius:50%;background:#8a8f96;display:block}
  .select-sm{position:absolute;top:8px;height:22px;background:#f3f6fa;font-size:11px;color:#333;padding:5px 10px;display:flex;justify-content:space-between;align-items:center}
  .select-sm::after{content:"";border:5px solid transparent;border-top:7px solid #222;border-bottom:0}
  .lang{left:811px;width:54px}
  .currency{left:878px;width:59px}
  .login{position:absolute;left:951px;top:7px;width:60px;height:24px;background:var(--green);color:#fff;font-size:11px;font-weight:700;display:flex;align-items:center;justify-content:center}
  .top-search{position:absolute;left:1027px;top:7px}
  .header{top:38px;height:55px;background:#fff}
  .brand{position:absolute;left:43px;top:10px;display:flex;align-items:center;gap:10px;font-size:32px;font-weight:700;color:var(--blue)}
  .brand i{width:32px;height:32px;background:var(--green);display:block}
  .destinations{position:absolute;left:907px;top:13px;width:145px;height:29px;border:1px solid #888;font-size:13px;color:#777;padding:6px 10px;display:flex;justify-content:space-between;align-items:center}
  .destinations::after{content:"";border:5px solid transparent;border-top:7px solid #222;border-bottom:0}
  .nav{top:93px;height:42px;background:var(--navy);border-bottom:1px solid #5d8fd0}
  .nav a{position:absolute;top:14px;color:#fff;font-size:12px;font-weight:700;text-decoration:none;letter-spacing:.2px}
  .hero{top:135px;height:461px;background:linear-gradient(180deg,#0c3a6f 0%,#2b6aa6 45%,#4d8b6e 72%,#12a8a6 80%,#0d8a8c 100%)}
  .hero h1{position:absolute;left:0;right:0;top:125px;text-align:center;color:#fff;font-size:48px;font-weight:900;text-shadow:0 3px 6px rgba(0,0,0,.5)}
  .search-panel{position:absolute;left:215px;top:222px;width:656px;height:57px;background:var(--green);padding:9px 13px;display:flex;box-shadow:0 3px 8px rgba(0,0,0,.3)}
  .search-panel .field{flex:1;background:var(--field);font-size:16px;color:#666;padding:10px 15px}
  .search-panel .go{width:56px;background:var(--blue);display:flex;align-items:center;justify-content:center}
  .about-title{position:absolute;left:55px;width:1095px;top:624px;text-align:center}
  .about-title::before{content:"";position:absolute;left:0;right:0;top:19px;border-top:1px solid var(--line)}
  .about-title h2{position:relative;display:inline-block;background:#fff;padding:0 2px;font-size:29px;font-weight:900;color:var(--blue)}
  .about-title h2 span{color:var(--green)}
  .about-text{position:absolute;left:160px;width:868px;top:679px;text-align:center;font-size:15.3px;line-height:20px;color:#222}
  .about-text p+p{margin-top:20px}
  .learn{position:absolute;left:539px;top:846px;width:127px;height:33px;background:var(--blue);color:#fff;font-size:15px;font-weight:500;display:flex;align-items:center;justify-content:center}
  .map{top:920px;height:280px;border-top:9px solid var(--blue);background:linear-gradient(90deg,#bcd9f5 0%,#c6e0fa 50%,#e6e6e2 72%,#e8e8e5 100%);box-shadow:0 -6px 8px rgba(0,0,0,.18)}
  .pin{position:absolute;left:538px;top:120px}
</style>
</head>
<body>
<div class="page">
  <div class="frame topbar">
    <div class="social"><span></span><span></span><span></span><span></span></div>
    <div class="select-sm lang">EN</div>
    <div class="select-sm currency">USD$</div>
    <div class="login">LOGIN</div>
    <svg class="top-search" width="24" height="24" viewBox="0 0 24 24"><circle cx="10" cy="10" r="7.5" fill="none" stroke="#0a6fd8" stroke-width="2.5"/><line x1="15.5" y1="15.5" x2="22" y2="22" stroke="#0a6fd8" stroke-width="2.8" stroke-linecap="round"/></svg>
  </div>
  <div class="frame header">
    <div class="brand"><i></i>IsleRoute</div>
    <div class="destinations">Destinations</div>
  </div>
  <nav class="frame nav">
    <a style="left:279px">DISCOVER CAYMAN</a>
    <a style="left:427px">THING TO DO</a>
    <a style="left:551px">MY TRIP PLAN</a>
    <a style="left:678px">MAP</a>
    <a style="left:747px">CONTACT US</a>
  </nav>
  <section class="frame hero" role="img" aria-label="Photo of a turquoise Caribbean sea with a palm-lined beach and resort under a blue sky">
    <h1>CAYMAN ISLANDS</h1>
    <div class="search-panel">
      <div class="field">Search Activities in the cayman Islands</div>
      <div class="go"><svg width="30" height="30" viewBox="0 0 24 24"><circle cx="10" cy="10" r="7.5" fill="none" stroke="#fff" stroke-width="2.2"/><line x1="15.5" y1="15.5" x2="22" y2="22" stroke="#fff" stroke-width="2.6" stroke-linecap="round"/></svg></div>
    </div>
  </section>
  <div class="about-title"><h2>About the <span>Cayman Islands</span></h2></div>
  <div class="about-text">
    <p>Located in the western Caribbean, The Cayman Islands is comprised of three islands; Grand Cayman, Cayman Brac and Little Cayman.&nbsp; It is easily accessible from Miami which is a mere 1-hour flight to Grand Cayman which is by far the largest and well known of the three islands, and the primary tourism destination of the three islands.</p>
    <p>It is an award-winning destination for its beaches, resorts, spa’s, restaurants and is considered a word class wedding and honey-moon destination.</p>
  </div>
  <div class="learn">Learn More</div>
  <section class="frame map" role="img" aria-label="Map of Grand Cayman with a location pin on the Cayman Islands">
    <svg class="pin" width="34" height="44" viewBox="0 0 34 44"><path d="M17 2a15 15 0 0 1 15 15c0 10-15 25-15 25S2 27 2 17A15 15 0 0 1 17 2z" fill="#e00000"/><circle cx="17" cy="16" r="8" fill="#fff"/></svg>
  </section>
</div>
</body>
</html>
```